I own a small business whose primary function is Professional Fashion and Commercial Photography and has a secondary function of Talent Management of Models/Actors. I've used PrintaNova in the past to print my own design, but I'd like something a bit more topical, fresh and done by an artist instead of a photographer (me).

My company logo is included with a few selected horizontal (landscape) photos of some of my models--I'd like to use a single model photo as the background for the entire card, either in color or converted to black and white, at opacity enough to see the photo but not too much to obscure any text or the company logo, or use a photo as a share of the card (not the entire background), or use all the three models on the card in some manor... Our company colors are white, black, grey-silver and red.

Industry/Entity Type

Small Business

Contact Information for Business Card

Darnell Voskuijl, Owner
KLT Studios
PO Box 7316
Millbrook VT 05999-7316
(555) 014-2273
dan@kltstudios-example,.com

```html
<!DOCTYPE html>
<html lang="en">
<head>
<meta charset="UTF-8">
<title>KLT Studios – Business Card</title>
<link href="https://fonts.googleapis.com/css2?family=Lato:wght@300;400;700;900&display=swap" rel="stylesheet">
<style>
  :root {
    --stage: #d9d9db;
    --ink: #1c1c1c;
    --ink-soft: #3a3a3a;
    --red: #e3262b;
    --panel: rgba(255, 255, 255, 0.86);
    --tile-teal: #8fa7a3;
    --tile-teal-dark: #5f7b7a;
    --tile-red: #c81e24;
    --tile-red-dark: #8e1418;
    --tile-purple: #6a4a8c;
    --tile-purple-dark: #3b2a52;
    --tile-slate: #4f6f84;
    --tile-slate-dark: #2d4556;
  }
  * { box-sizing: border-box; margin: 0; padding: 0; }
  html, body {
    width: 1200px; height: 926px; overflow: hidden;
    background: var(--stage);
    font-family: 'Lato', sans-serif;
    color: var(--ink);
  }
  .stage {
    position: relative; width: 1200px; height: 926px;
    display: flex; align-items: center; justify-content: center; gap: 52px;
  }
  .card {
    position: relative; overflow: hidden;
    box-shadow: 0 10px 28px rgba(0,0,0,0.22);
  }
  .card--front { width: 380px; height: 665px; }
  .card--back { width: 665px; height: 380px; }

  .photo-grid {
    position: absolute; inset: 0;
    display: grid; grid-template-columns: 1fr 1fr; grid-template-rows: 1fr 1fr;
  }
  .photo-tile { width: 100%; height: 100%; }
  .photo-tile--teal { background: linear-gradient(135deg, var(--tile-teal), var(--tile-teal-dark)); }
  .photo-tile--red { background: linear-gradient(135deg, var(--tile-red), var(--tile-red-dark)); }
  .photo-tile--purple { background: linear-gradient(135deg, var(--tile-purple), var(--tile-purple-dark)); }
  .photo-tile--slate { background: linear-gradient(135deg, var(--tile-slate), var(--tile-slate-dark)); }

  .info-panel {
    position: absolute; left: 22px; right: 22px; top: 30px; bottom: 30px;
    background: var(--panel);
    padding: 34px 30px;
    display: flex; flex-direction: column;
  }
  .brand-name { font-size: 26px; font-weight: 400; color: var(--ink); letter-spacing: 0.5px; }
  .brand-rule { height: 1px; background: var(--red); margin: 12px 0 20px; }

  .person-name { font-size: 27px; text-transform: uppercase; letter-spacing: 0.5px; line-height: 1.1; }
  .person-name .first { font-weight: 900; }
  .person-name .last { font-weight: 300; }
  .person-role { color: var(--red); font-size: 21px; font-weight: 700; margin-top: 4px; }
  .services { font-size: 16px; line-height: 1.3; color: var(--ink-soft); margin-top: 14px; text-align: right; }
  .divider { height: 1px; background: var(--ink); margin: 20px 0 26px 40px; }

  .contact-list { list-style: none; display: flex; flex-direction: column; gap: 22px; }
  .contact-item { display: flex; gap: 12px; align-items: flex-start; font-size: 18px; line-height: 1.25; }
  .contact-icon { width: 18px; height: 18px; flex: none; margin-top: 3px; fill: var(--ink); }
</style>
</head>
<body>
<main class="stage">

  <section class="card card--front" aria-label="Business card front">
    <div class="photo-grid">
      <div class="photo-tile photo-tile--teal" role="img" aria-label="Model portrait, blond young man in blue shirt"></div>
      <div class="photo-tile photo-tile--red" role="img" aria-label="Model portrait, young man in red t-shirt"></div>
      <div class="photo-tile photo-tile--purple" role="img" aria-label="Model portrait, young man with sunglasses on purple"></div>
      <div class="photo-tile photo-tile--slate" role="img" aria-label="Model portrait, young man in plaid shirt"></div>
    </div>

    <div class="info-panel">
      <div class="brand">
        <span class="brand-name">KLT Studios</span>
      </div>
      <div class="brand-rule"></div>

      <h1 class="person-name"><span class="first">Darnell</span> <span class="last">Voskuijl</span></h1>
      <p class="person-role">owner</p>
      <p class="services">Pro Fashion &amp;<br>Commercial Photography<br>and Talent Management</p>
      <div class="divider"></div>

      <ul class="contact-list">
        <li class="contact-item">
          <svg class="contact-icon" viewBox="0 0 24 24" aria-hidden="true"><path d="M6.6 10.8a15.1 15.1 0 0 0 6.6 6.6l2.2-2.2a1 1 0 0 1 1-.25 11.4 11.4 0 0 0 3.6.57 1 1 0 0 1 1 1V20a1 1 0 0 1-1 1A17 17 0 0 1 3 4a1 1 0 0 1 1-1h3.5a1 1 0 0 1 1 1c0 1.25.2 2.45.57 3.57a1 1 0 0 1-.25 1z"/></svg>
          <span>05999-7316<br>(555) 014-2273</span>
        </li>
        <li class="contact-item">
          <svg class="contact-icon" viewBox="0 0 24 24" aria-hidden="true"><path d="M2 5h20v14H2zm2 2v.4l8 5.2 8-5.2V7zm16 10V9.8l-8 5.2-8-5.2V17z"/></svg>
          <span>dan@kltstudios-example.com</span>
        </li>
        <li class="contact-item">
          <svg class="contact-icon" viewBox="0 0 24 24" aria-hidden="true"><path d="M12 2a7 7 0 0 0-7 7c0 5 7 13 7 13s7-8 7-13a7 7 0 0 0-7-7zm0 9.5A2.5 2.5 0 1 1 12 6.5a2.5 2.5 0 0 1 0 5z"/></svg>
          <span>PO Box 7316 Millbrook VT<br>05999-7316</span>
        </li>
      </ul>
    </div>
  </section>

  <section class="card card--back" aria-label="Business card back">
    <div class="photo-grid">
      <div class="photo-tile photo-tile--teal" role="img" aria-label="Model portrait, blond young man in blue shirt"></div>
      <div class="photo-tile photo-tile--red" role="img" aria-label="Model portrait, young man in red t-shirt"></div>
      <div class="photo-tile photo-tile--purple" role="img" aria-label="Model portrait, young man with sunglasses on purple"></div>
      <div class="photo-tile photo-tile--slate" role="img" aria-label="Model portrait, young man in plaid shirt"></div>
    </div>
  </section>

</main>
</body>
</html>
```